Online Psychology Practice needs business cards.

Online Psychology service needs business cards. Have own logo- please see uploaded. I have other file formats if you need (not sure one needed?)

Details for Business Card:
Fiona Kettlewood
Clinical Psychologist BPsych, BPsych (Hons), MPsych (Clin), MAPS
T: 0457260714 | F: 08 71526804
E: hello@harbourlightmindcarestudio.com.au
W: harbourlightmindcarestudio.com.au

Industry/Entity Type

Health

Contact Information for Business Card

Logo plus details above (couldn't write in this section)

```html
<!DOCTYPE html>
<html lang="en">
<head>
<meta charset="utf-8">
<title>Harbourlight Mind Care Studio – Business Cards</title>
<link href="https://fonts.googleapis.com/css2?family=Cinzel:wght@600;700&family=Roboto+Condensed:wght@400&display=swap" rel="stylesheet">
<style>
  :root {
    --backdrop: #6a6768;
    --card: #fbfbfb;
    --navy: #1d4a70;
    --navy-deep: #173f62;
    --teal: #1d7a9b;
    --sky: #4a8fc8;
    --ink: #2b2b2b;
    --muted: #3a3a3a;
  }
  * { box-sizing: border-box; margin: 0; padding: 0; }
  html, body { width: 1200px; height: 1200px; overflow: hidden; }
  body {
    background: var(--backdrop);
    position: relative;
    font-family: "Roboto Condensed", Arial, sans-serif;
  }
  .card {
    position: absolute;
    left: 306px;
    width: 588px;
    height: 348px;
    background: var(--card);
    border-radius: 18px;
    overflow: hidden;
  }
  .card--front { top: 200px; }
  .card--back { top: 636px; }

  /* Front */
  .brand {
    font-family: "Cinzel", Georgia, serif;
    font-weight: 700;
    color: var(--navy);
    text-align: center;
    letter-spacing: 1px;
  }
  .card--front .brand {
    position: absolute;
    left: 0; right: 0;
    top: 150px;
    font-size: 30px;
    line-height: 1.15;
  }
  .brand-dot {
    display: block;
    width: 46px; height: 46px;
    border-radius: 50%;
    background: var(--navy);
    margin: 0 auto 16px;
  }
  .card--front .brand-dot {
    position: absolute;
    left: 271px; top: 78px;
    margin: 0;
  }
  .front-web {
    position: absolute;
    left: 0; right: 0;
    top: 294px;
    text-align: center;
    font-size: 16px;
    color: var(--ink);
  }
  .front-web .accent, .contact .accent { color: var(--teal); }
  .front-band {
    position: absolute;
    left: 0; right: 0; bottom: 0;
    height: 9px;
    display: flex;
  }
  .front-band span:first-child { flex: 1; background: var(--navy); }
  .front-band span:last-child { flex: 1; background: var(--teal); }

  /* Back */
  .back-panel { position: absolute; left: 0; top: 0; }
  .card--back .brand {
    position: absolute;
    right: 26px;
    top: 40px;
    width: 300px;
    text-align: right;
    font-size: 25px;
    line-height: 1.15;
  }
  .person {
    position: absolute;
    right: 26px;
    top: 146px;
    text-align: right;
  }
  .person-name {
    font-family: "Cinzel", Georgia, serif;
    font-weight: 600;
    font-size: 22px;
    letter-spacing: 1.5px;
    color: var(--ink);
    text-transform: uppercase;
  }
  .person-role {
    font-size: 15px;
    color: var(--teal);
    margin-top: 4px;
  }
  .person-quals {
    font-size: 13.5px;
    color: var(--muted);
    line-height: 1.4;
    margin-top: 2px;
  }
  .contact {
    position: absolute;
    right: 26px;
    top: 262px;
    list-style: none;
    font-size: 13.5px;
    color: var(--ink);
    text-align: right;
  }
  .contact li {
    display: flex;
    justify-content: flex-end;
    align-items: center;
    gap: 8px;
    height: 20px;
  }
  .icon { width: 12px; height: 12px; fill: var(--teal); flex: none; }
  .phone-pair { margin-right: 4px; }
</style>
</head>
<body>

<section class="card card--front">
  <span class="brand-dot"></span>
  <h1 class="brand">Harbourlight<br>Mind Care Studio</h1>
  <p class="front-web">www.harbourlight<span class="accent">mindcare</span>studio.com.au</p>
  <div class="front-band"><span></span><span></span></div>
</section>

<section class="card card--back">
  <svg class="back-panel" width="260" height="348" viewBox="0 0 260 348" aria-hidden="true">
    <path d="M0 0 H184 Q290 174 184 348 H0 Z" fill="var(--sky)"/>
    <path d="M0 0 H170 Q276 174 178 348 H0 Z" fill="var(--navy)"/>
  </svg>

  <h2 class="brand">Harbourlight<br>Mind Care Studio</h2>

  <div class="person">
    <p class="person-name">Fiona Kettlewood</p>
    <p class="person-role">Clinical Psychologist</p>
    <p class="person-quals">BPsych, BPsych (Hons),<br>MPsych (Clin), MAPS</p>
  </div>

  <ul class="contact">
    <li>
      <span>0457260714</span>
      <svg class="icon phone-pair" viewBox="0 0 12 12"><rect x="3" y="0" width="6" height="3"/><rect x="0" y="3.5" width="12" height="5" rx="1"/><rect x="3" y="7" width="6" height="5"/></svg>
      <span>08 71526804</span>
      <svg class="icon" viewBox="0 0 12 12"><path d="M1 4 Q6 0 11 4 L9 6 L8 4.5 H4 L3 6 Z"/><path d="M2 7 H10 L11 11 H1 Z"/></svg>
    </li>
    <li>
      <span>hello@harbourlightmindcarestudio.com.au</span>
      <svg class="icon" viewBox="0 0 12 12"><path d="M0 2 H12 V3 L6 7 L0 3 Z"/><path d="M0 4.5 L6 8.5 L12 4.5 V10 H0 Z"/></svg>
    </li>
    <li>
      <span>www.harbourlight<span class="accent">mindcare</span>studio.com.au</span>
      <svg class="icon" viewBox="0 0 12 12"><circle cx="6" cy="6" r="5.5"/><path d="M0.5 6 H11.5 M6 0.5 V11.5 M6 0.5 Q2.5 6 6 11.5 M6 0.5 Q9.5 6 6 11.5" stroke="#fff" stroke-width="0.8" fill="none"/></svg>
    </li>
  </ul>
</section>

</body>
</html>
```